Redesign of Plastic Surgeon Website to fully responsive / modern feel

Hi

Our current website is out of date www.harbourlinecosmetic.org

We want a fresh / modern looking design
Needs to be fully responsive design that works extremely well on ipad and mobile device

Would like design for both full screen website and mobile

Have listed a few websites of other plastic surgeons we like
http://www.reformclinicdaily.com/
http://www.peterholtbymd.com/
http://www.corvanbeauty.com/
http://www.tidewellcontouring.com/

Menu needs to include
1. About Us
2. Procedures (see current website for example)
3. News
4. Patient Resources
5. Contact Us

We are flexible with colours / images / layout

I have uploaded a document that has some content - the face pages content is completed only

some of the procedures can have content upwards of 4000 words - total website can be large with over 40,000 words
Updates

Target Market(s)

Mainly women 20-60 85% of practice
Some men 15%

Industry/Entity Type

Plastic Surgery

Number of Pages Required

5+ page

Requirements
Must have
• We need designs for
• Homepage
• Internal pages
• 1. Landing pages for breast / body / face / non surgical main pages
• 2. Procedure pages for individual pages under each section - eg breast augmentation
• 3. About us pages - like meet the doctor, our staff, clinics
• 4. Contact page
• 5. Blog / News page
Nice to have
• See our list of websites for examples of designs we like
• Like full screen design with nice hero image
• Needs to have good to call to action messages on home page like
• Specials, procedure of the month, etc

```html
<!DOCTYPE html>
<html lang="en">
<head>
<meta charset="utf-8">
<title>About Us – Harbourline Cosmetic</title>
<link rel="stylesheet" href="https://fonts.googleapis.com/css2?family=Roboto:wght@300;400;500;700&family=Open+Sans:wght@400;600&display=swap">
<style>
:root{
  --pink:#d93c9e;
  --pink-dark:#c52f8d;
  --pink-light:#de4aa6;
  --ink:#2f2f2f;
  --muted:#8a8a8a;
  --soft:#f1f1f1;
  --footer:#333333;
  --white:#ffffff;
}
*{box-sizing:border-box;margin:0;padding:0}
html,body{width:781px;height:1200px;overflow:hidden}
body{font-family:"Roboto",Arial,sans-serif;color:var(--ink);background:var(--white);position:relative}
ul{list-style:none}

/* header */
.site-header{position:relative;height:68px;background:var(--white);z-index:2}
.brand{position:absolute;left:35px;top:29px;display:flex;align-items:center;gap:5px;
  font-size:10px;font-weight:500;color:var(--ink);white-space:nowrap}
.brand-mark{width:9px;height:9px;background:var(--pink);display:block}
.topbar{position:absolute;left:160px;right:22px;top:7px;height:14px;display:flex;justify-content:space-between;align-items:center}
.topbar .info{font-size:7px;font-weight:500;color:#555;letter-spacing:.3px}
.topbar .social{display:flex;gap:9px;align-items:center}
.dot-icon{width:7px;height:7px;border-radius:50%;background:#444;display:block}
.main-nav{position:absolute;left:160px;right:22px;top:36px;display:flex;justify-content:space-between}
.main-nav a{font-size:7.4px;font-weight:500;color:#333;text-decoration:none;text-transform:uppercase;text-align:center;line-height:1.25}

/* hero */
.page-hero{position:relative;height:180px;background:radial-gradient(ellipse at 50% 40%,#8a8a8a 0%,#555 45%,#2c2c2c 100%);
  display:flex;flex-direction:column;align-items:center;justify-content:center;color:var(--white)}
.page-hero h1{font-size:32px;font-weight:400;letter-spacing:1px;margin-top:8px}
.breadcrumb{font-size:7px;font-weight:500;margin-top:6px;text-transform:uppercase;display:flex;gap:6px;align-items:center}

/* intro */
.intro{height:172px;background:var(--soft);text-align:center;padding-top:48px}
.section-title{font-size:13px;font-weight:400;letter-spacing:.5px;text-transform:uppercase;color:var(--ink)}
.intro p{width:540px;margin:20px auto 0;font-family:"Open Sans",Arial,sans-serif;font-size:6.4px;line-height:1.75;color:var(--muted)}
.pager{display:flex;justify-content:center;gap:5px;margin-top:14px}
.pager span{width:6px;height:6px;border-radius:50%;border:1px solid #333}
.pager span.active{background:#333}

/* team */
.team{height:442px;text-align:center;padding-top:24px}
.team-grid{display:flex;gap:18px;padding:0 37px;margin-top:24px}
.member{width:223px}
.member-photo{height:272px;position:relative}
.photo-a{background:linear-gradient(160deg,#efefef,#cfcfcf)}
.photo-b{background:radial-gradient(ellipse at 50% 45%,#bdbdbd 0%,#8a8a8a 45%,#e9e9e9 100%)}
.photo-c{background:radial-gradient(ellipse at 50% 45%,#b07e74 0%,#6c3a3b 45%,#2a1c1f 100%)}
.member-overlay{position:absolute;inset:0;background:rgba(255,255,255,.82);padding:80px 26px 0;display:flex;flex-direction:column;align-items:center}
.member-overlay h3{font-size:10px;font-weight:500;letter-spacing:1.5px;text-transform:uppercase;color:#444}
.member-overlay .role{font-size:7px;color:var(--muted);margin-top:3px;letter-spacing:.5px}
.member-overlay p{font-family:"Open Sans",Arial,sans-serif;font-size:6.4px;line-height:1.7;color:#777;margin-top:12px}
.member-overlay .social{display:flex;gap:10px;margin-top:14px}
.member-name{font-size:10px;font-weight:400;letter-spacing:1.5px;text-transform:uppercase;color:#555;margin-top:14px}
.member-role{font-size:7px;color:var(--muted);margin-top:3px;letter-spacing:.5px}

/* contact band */
.contact-band{display:flex;height:74px;margin:0 37px;position:relative;z-index:1}
.band-item{flex:1;display:flex;align-items:center;gap:14px;padding-left:22px;color:var(--white)}
.band-item:nth-child(1){background:var(--pink)}
.band-item:nth-child(2){background:var(--pink-dark)}
.band-item:nth-child(3){background:var(--pink-light)}
.band-item h4{font-size:8px;font-weight:500;text-transform:uppercase;letter-spacing:.3px}
.band-item p{font-size:6.6px;line-height:1.5;margin-top:3px}

/* footer */
.site-footer{position:absolute;left:0;right:0;top:898px;bottom:0;background:var(--footer);color:#ccc}
.footer-brand{position:absolute;left:52px;top:130px;display:flex;align-items:center;gap:5px;font-size:10px;font-weight:500;color:#ccc;white-space:nowrap}
.footer-col h5{font-size:11px;font-weight:400;color:var(--white);text-transform:uppercase}
.footer-col h5::after{content:"";display:block;width:40px;height:2px;background:var(--pink);margin-top:6px}
.services{position:absolute;left:288px;top:66px}
.service-lists{display:flex;gap:48px;margin-top:16px}
.service-lists li{font-size:6.6px;color:#bbb;line-height:20px}
.service-lists li::before{content:"›";margin-right:4px}
.newsletter{position:absolute;left:540px;top:66px;width:200px}
.newsletter p{font-family:"Open Sans",Arial,sans-serif;font-size:6.4px;line-height:1.6;margin-top:14px;color:#bbb}
.subscribe{display:flex;margin-top:12px}
.subscribe span{flex:1;height:22px;background:var(--white);color:#444;font-size:6.6px;display:flex;align-items:center;padding-left:10px}
.subscribe b{width:60px;height:22px;background:var(--pink);color:var(--white);font-size:7px;font-weight:500;display:flex;align-items:center;justify-content:center}
.newsletter h6{font-size:6.8px;font-weight:500;color:var(--white);margin-top:14px;text-transform:uppercase}
.newsletter .social{display:flex;gap:18px;margin-top:16px}
.newsletter .dot-icon{background:#bbb}
.footer-bottom{position:absolute;left:0;right:0;top:262px;text-align:center;font-size:6.6px;color:#aaa}
.footer-bottom nav{margin-top:10px;font-size:8px;letter-spacing:1.2px;color:#bbb}
</style>
</head>
<body>

<header class="site-header">
  <div class="brand"><span class="brand-mark"></span>Harbourline Cosmetic</div>
  <div class="topbar">
    <span class="info">INFO &amp; RESERVATIONS : 02 5550 1700</span>
    <div class="social">
      <span class="dot-icon"></span><span class="dot-icon"></span><span class="dot-icon"></span><span class="dot-icon"></span><span class="dot-icon"></span>
      <svg width="9" height="9" viewBox="0 0 10 10"><circle cx="4" cy="4" r="3" fill="none" stroke="#333" stroke-width="1.4"/><line x1="6.2" y1="6.2" x2="9.2" y2="9.2" stroke="#333" stroke-width="1.4"/></svg>
    </div>
  </div>
  <nav class="main-nav">
    <a href="#">Our Practice</a>
    <a href="#">Surgical<br>Procedures</a>
    <a href="#">News &amp; Views</a>
    <a href="#">Before After Photos</a>
    <a href="#">Plastic<br>Surgery Reviews</a>
    <a href="#">Patient<br>Preparation</a>
    <a href="#">FAQ</a>
    <a href="#">Contact</a>
  </nav>
</header>

<section class="page-hero" role="img" aria-label="Black and white portrait photograph behind the page title">
  <h1>ABOUT US</h1>
  <div class="breadcrumb"><span>Home</span>
    <svg width="5" height="6" viewBox="0 0 5 6"><path d="M0 0L5 3L0 6Z" fill="#d93c9e"/></svg>
    <span>About Us</span></div>
</section>

<section class="intro">
  <h2 class="section-title">What We Do Everday</h2>
  <p>Vivamus congue est tellus et lobortis dictum a magna mollis, finibus felis id, aliquet ligula. Donec nec mattis dolor, sit amet condimentum mi. Ut et turpis sit amet leo egestas sagittis ac sagittis lectus. Curabitur dignissim consequat nisi, nec iaculis neque auctor a. Proin faucibus viverra nisl, eu suscipit diam suscipit id. There are many variations of passages available, but most have suffered alteration in some form by injected humour.</p>
  <div class="pager"><span class="active"></span><span></span><span></span></div>
</section>

<section class="team">
  <h2 class="section-title">Meet Our Entire Team</h2>
  <div class="team-grid">
    <article class="member">
      <div class="member-photo photo-a" role="img" aria-label="Portrait photograph of a team member">
        <div class="member-overlay">
          <h3>Owen Hartley</h3>
          <span class="role">Photography</span>
          <p>We'll walk you through every option, plan your recovery with care and stay beside you from the very first visit to your final review.</p>
          <div class="social"><span class="dot-icon"></span><span class="dot-icon"></span><span class="dot-icon"></span><span class="dot-icon"></span></div>
        </div>
      </div>
    </article>
    <article class="member">
      <div class="member-photo photo-b" role="img" aria-label="Black and white portrait photograph of a team member"></div>
      <h3 class="member-name">Miles Carrow</h3>
      <span class="member-role">Photography</span>
    </article>
    <article class="member">
      <div class="member-photo photo-c" role="img" aria-label="Colour portrait photograph of a team member"></div>
      <h3 class="member-name">Miles Carrow</h3>
      <span class="member-role">Photography</span>
    </article>
  </div>
</section>

<section class="contact-band">
  <div class="band-item">
    <svg width="14" height="18" viewBox="0 0 14 18"><path d="M7 0C3.1 0 0 3.1 0 7c0 5 7 11 7 11s7-6 7-11c0-3.9-3.1-7-7-7z" fill="#fff"/><circle cx="7" cy="7" r="2.6" fill="#d93c9e"/></svg>
    <div><h4>Hospital Address</h4><p>48 Harbour Lane, Bay Corner<br>Melbourne - VIC</p></div>
  </div>
  <div class="band-item">
    <svg width="16" height="16" viewBox="0 0 16 16"><path d="M3.2 1l2.6 3.2-1.6 2a9 9 0 0 0 5.6 5.6l2-1.6L15 12.8 13.2 15C6.6 15 1 9.4 1 2.8z" fill="#fff"/></svg>
    <div><h4>Emergency ( 24x7 )</h4><p>02 5550 1700<br>Call Us Now: 24/7 Customer Support</p></div>
  </div>
  <div class="band-item">
    <svg width="18" height="13" viewBox="0 0 18 13"><rect x="1" y="1" width="16" height="11" fill="none" stroke="#fff" stroke-width="1.6"/><path d="M1 1l8 6 8-6" fill="none" stroke="#fff" stroke-width="1.6"/></svg>
    <div><h4>Hospital Address</h4><p>info@harbourline.org<br>care@harbourline.org</p></div>
  </div>
</section>

<footer class="site-footer">
  <div class="footer-brand"><span class="brand-mark"></span>Harbourline Cosmetic</div>
  <div class="footer-col services">
    <h5>Our Services</h5>
    <div class="service-lists">
      <ul><li>Botox</li><li>Pulmonary</li><li>Cardiology</li><li>Neurology</li><li>Traumatology</li><li>Neurology</li></ul>
      <ul><li>Dental</li><li>Nuclear magnetic</li><li>Pregnancy</li><li>For Disabled</li><li>X-ray</li><li>Prosthesis</li></ul>
    </div>
  </div>
  <div class="footer-col newsletter">
    <h5>Newsletter</h5>
    <p>Subscribe for clinic news, seasonal specials and our procedure of the month.</p>
    <div class="subscribe"><span>Email Address</span><b>SEND</b></div>
    <h6>Stay Connected</h6>
    <div class="social"><span class="dot-icon"></span><span class="dot-icon"></span><span class="dot-icon"></span><span class="dot-icon"></span></div>
  </div>
  <div class="footer-bottom">
    <p>© Harbourline Cosmetic Dr Lena Marsh Plastic Surgery Sydney Australia</p>
    <nav>Home | Disclaimer | Privacy | Sitemap | Feedback | Tell a Friend | Contact Us | Find us online</nav>
  </div>
</footer>

</body>
</html>
```